Redesign/Facelift for Affiliate Shopping Fashion Site

We are velunix, Fashion web site from Berlin, Germany,
looking to redesign/facelift our affiliate shopping site,
http://shop.velunix.de/bekleidung,84rtpa21xuwdnc90,ec_sale,sa
(Main page view)
http://shop.velunix.de/lorn-gale-seidentunika-pemby,3kdh5w1rcyt8ae6v,i
(Single article view)

Altogether we want to make it more coherent, key words being
MINIMAL and STYLISH.

NOTE:
You don´t need to completely design both pages, it would be sufficient to propose a direction you would take. However, we should be able to envision the complete solution.

The solution should be similar to another comparable affiliate site,
http://www.kaufzirkel.de/browse/damen-kleidung

- - General Brief:
The design should have an overall aesthetic coherence,
especially when it comes to sizes of elements
and the bars like in the side bar left, or "Zum Shop".
The solution should be done for the main page and the single article page.

- - Here are the elements in particular, and how they should be designed:
- Main Page HEADER BAR (and single article page) elements:
header bar extends across the entire width of the screen
our logo
"Shopping" text next to the logo
search form
categories "Bekleidung, Accessoires, Schmuck" etc.
Plimbora and zappel buttons

- Main page SIDEBAR (left):
elements as can be seen
menu "Preis" is replaced by a price "slider" to more accurately determine
a shopping price range

- Main page PRODUCTS:
elements as can be seen
the "% discount" symbol and "Zum Shop" elements especially
should be looked at

- Main page (and single article page) FOOTER:
should extend across the entire width of the screen

- Single article page
(http://shop.velunix.de/lorn-gale-seidentunika-pemby,3kdh5w1rcyt8ae6v,i)
header and footer as discussed for the Main page
bars (below the article) "Ähnliche Produkte zu….", "Weitere Produkte…" should be replaced by
"lighter" solution

Thank you,
feel free to ask question if something is not clear.
Telmo

```html
<!DOCTYPE html>
<html lang="de">
<head>
<meta charset="utf-8">
<title>velunix Shopping</title>
<link href="https://fonts.googleapis.com/css2?family=Open+Sans:wght@300;400;600;700;800&display=swap" rel="stylesheet">
<style>
:root{
  --ink:#2a0a0f;
  --band:#561821;
  --accent:#7e1424;
  --badge:#a8253a;
  --button:#b3263a;
  --page:#f7f7f7;
  --card:#ffffff;
  --line:#e2e2e2;
  --text:#222222;
  --muted:#555555;
}
*{box-sizing:border-box;margin:0;padding:0}
html,body{width:783px;height:1200px;overflow:hidden}
body{position:relative;background:var(--page);font-family:"Open Sans",Arial,sans-serif;color:var(--text);letter-spacing:-0.3px}
.header{position:absolute;left:0;top:0;width:783px;height:98px;background:var(--ink)}
.brand{position:absolute;left:29px;top:17px;display:flex;align-items:baseline;gap:10px;color:#fff}
.brand-name{font-size:24px;font-weight:800;letter-spacing:1px;text-transform:uppercase}
.brand-tag{font-size:10px;font-weight:400}
.search{position:absolute;left:292px;top:19px;width:312px;height:30px;background:#120205;border:1px solid #3a1016;display:flex;align-items:center;padding-left:8px}
.search span{font-size:11px;color:#eee;flex:1}
.search b{font-weight:400;font-size:11px;color:#fff;background:var(--accent);height:22px;line-height:22px;padding:0 15px;margin-right:4px}
.social{position:absolute;top:26px;display:flex;gap:6px;left:633px}
.social span{display:flex;align-items:center;gap:4px;height:16px;padding:0 6px;font-size:9px;color:#fff;background:var(--accent)}
.social i{width:6px;height:6px;background:#fff;display:block}
.nav{position:absolute;left:31px;top:67px;display:flex;gap:15px;font-size:11.5px;color:#fff}
.subbar{position:absolute;left:0;top:98px;width:783px;height:42px;background:var(--band)}
.subbar .crumb{position:absolute;left:31px;top:12px;font-size:11px;color:#fff;font-weight:600}
.price{position:absolute;left:539px;top:8px;display:flex;align-items:center;gap:10px;font-size:11px;color:#fff}
.price .select{width:183px;height:26px;background:#6a1f2a;border:1px solid #7a2a35;display:flex;align-items:center;justify-content:space-between;padding:0 8px;font-size:10.5px}
.sidebar{position:absolute;left:0;top:140px;width:152px;height:263px;background:var(--ink);z-index:2;padding:20px 0 0 39px}
.sidebar::before{content:"";position:absolute;left:44px;top:0;border:6px solid transparent;border-top-color:var(--band)}
.sidebar li{list-style:none;font-size:10.5px;color:#fff;height:25.6px}
.hero{position:absolute;left:30px;top:163px;width:722px;height:257px;background:linear-gradient(90deg,#6b6b6b,#d6d6d6 35%,#9a9a9a 55%,#3a3a3a 80%,#1a1a1a)}
.hero-card{position:absolute;left:505px;top:61px;width:190px;height:138px;background:#fff;text-align:center;padding-top:14px}
.hero-card .t1{font-size:29px;font-weight:300;color:var(--accent);line-height:30px}
.hero-card .t2{font-size:28px;font-weight:800;color:var(--ink);line-height:28px;letter-spacing:-1px}
.hero-card .t3{font-size:12px;color:var(--accent);margin-top:10px}
.hero-card .buy{display:inline-block;margin-top:3px;background:var(--accent);color:#fff;font-size:10px;font-weight:700;padding:3px 13px}
.dots{position:absolute;left:336px;top:240px;display:flex;gap:5px}
.dots i{width:10px;height:10px;border-radius:50%;background:#fff;display:block}
.dots i:first-child{background:var(--ink)}
.heading{position:absolute;left:0;top:427px;width:783px;text-align:center;font-size:28px;font-weight:300;color:var(--ink);letter-spacing:-1px}
.rule{position:absolute;left:30px;top:485px;width:722px;height:1px;background:var(--line)}
.card{position:absolute;width:174px;height:281px;background:var(--card);border:1px solid var(--line);text-align:center}
.badge{position:absolute;right:5px;top:13px;width:44px;height:44px;border-radius:50%;background:var(--badge);color:#fff;font-size:14px;line-height:44px;border:2px dotted #fff;outline:2px solid var(--badge)}
.photo{position:absolute;top:28px;left:50%;transform:translateX(-50%)}
.name{position:absolute;top:176px;width:100%;font-size:11px;font-weight:700}
.sub{position:absolute;top:191px;width:100%;font-size:10.5px;color:var(--muted)}
.plabel{position:absolute;top:209px;width:100%;font-size:10.5px;font-weight:700}
.prices{position:absolute;top:224px;width:100%;font-size:10px}
.prices s{color:var(--muted)}
.shop{position:absolute;top:241px;left:50%;transform:translateX(-50%);background:var(--button);color:#fff;font-size:10.5px;font-weight:700;padding:3px 7px;white-space:nowrap}
.more{position:absolute;left:321px;top:1088px;width:142px;height:31px;background:var(--ink);color:#fff;font-size:10.5px;font-weight:700;display:flex;align-items:center;justify-content:center;gap:5px}
.more i{width:12px;height:12px;border-radius:50%;background:var(--badge);display:flex;align-items:center;justify-content:center}
.footer{position:absolute;left:0;top:1132px;width:783px;height:68px;background:var(--ink);color:#fff}
.footer .brand-name{position:absolute;left:36px;top:10px;font-size:22px}
.footer .copy{position:absolute;left:36px;top:45px;font-size:10.5px}
.footer .links{position:absolute;right:30px;top:15px;font-size:10.5px;word-spacing:2px}
.footer .note{position:absolute;right:30px;top:42px;font-size:10.5px}
</style>
</head>
<body>
<header class="header">
  <div class="brand"><span class="brand-name">velunix</span><span class="brand-tag">SHOPPING</span></div>
  <div class="search"><span>Wanna Search Here ?</span><b>Search</b></div>
  <div class="social"><span><i></i>Plimbora</span><span><i></i>zappel</span></div>
  <nav class="nav"><span>Bekleidung</span><span>Accessoires</span><span>Schmuck</span><span>Schuhe</span><span>Taschen</span><span>Uhren</span><span>Beauty</span><span>Wohnen</span><span>Haushalt</span><span>Drogerie</span><span>Sport und Freizeit</span><span>Spielzeug</span></nav>
</header>
<div class="subbar">
  <span class="crumb">Bekleidung</span>
  <div class="price">Price<div class="select"><span>0€ - 25 €</span><svg width="10" height="7" viewBox="0 0 10 7"><path d="M1 1l4 4 4-4" stroke="#fff" stroke-width="2" fill="none"/></svg></div></div>
</div>
<ul class="sidebar">
  <li>Sex</li><li>Categories</li><li>Brand</li><li>Price</li><li>% Sale</li><li>Color</li><li>Material</li><li>Pattern</li><li>Shops</li>
</ul>
<section class="hero" role="img" aria-label="Black and white fashion photo of a model seated by a window in a hotel room">
  <div class="hero-card"><div class="t1">VELUNIX</div><div class="t2">FASHIONS</div><div class="t3">SHOPPING</div><span class="buy">BUY NOW</span></div>
  <div class="dots"><i></i><i></i><i></i><i></i><i></i></div>
</section>
<h2 class="heading">PRODUCTS</h2>
<div class="rule"></div>

<div class="card" style="left:30px;top:500px"><div class="photo" role="img" aria-label="Beige blazer" style="width:92px;height:135px;background:linear-gradient(#efe6d4,#d9cbb0)"></div><div class="badge">30%</div><div class="name">Marla Quinn</div><div class="sub">Blazer, sand</div><div class="plabel">Price</div><div class="prices"><s>89.90 €</s> 74.99 € *</div><span class="shop">ZUM SHOP</span></div>
<div class="card" style="left:213px;top:500px"><div class="photo" role="img" aria-label="Yellow sleeveless dress" style="width:60px;height:130px;background:linear-gradient(#f1e56a,#e8dc4c)"></div><div class="badge">30%</div><div class="name">Marla Quinn</div><div class="sub">Blazer, sand</div><div class="plabel">Price</div><div class="prices"><s>89.90 €</s> 74.99 € *</div><span class="shop">ZUM SHOP</span></div>
<div class="card" style="left:395px;top:500px"><div class="photo" role="img" aria-label="White leather biker jacket" style="width:102px;height:140px;background:linear-gradient(#f2f2f2,#dcdcdc)"></div><div class="badge">30%</div><div class="name">Marla Quinn</div><div class="sub">Blazer, sand</div><div class="plabel">Price</div><div class="prices"><s>89.90 €</s> 74.99 € *</div><span class="shop">ZUM SHOP</span></div>
<div class="card" style="left:577px;top:500px"><div class="photo" role="img" aria-label="Floral print trousers" style="width:40px;height:135px;background:linear-gradient(#8aa0d8,#d88aa8,#6f88c8)"></div><div class="badge">30%</div><div class="name">Marla Quinn</div><div class="sub">Blazer, sand</div><div class="plabel">Price</div><div class="prices"><s>89.90 €</s> 74.99 € *</div><span class="shop">ZUM SHOP</span></div>

<div class="card" style="left:30px;top:789px"><div class="photo" role="img" aria-label="Patterned grey shorts" style="width:94px;height:80px;top:75px;background:linear-gradient(#cfcac2,#a9a49c)"></div><div class="badge">30%</div><div class="name">Marla Quinn</div><div class="sub">Blazer, sand</div><div class="plabel">Price</div><div class="prices"><s>89.90 €</s> 74.99 € *</div><span class="shop">ZUM SHOP</span></div>
<div class="card" style="left:213px;top:789px"><div class="photo" role="img" aria-label="Blue suede jacket" style="width:92px;height:118px;top:38px;background:linear-gradient(#8fa0b4,#6f8296)"></div><div class="badge">30%</div><div class="name">Marla Quinn</div><div class="sub">Blazer, sand</div><div class="plabel">Price</div><div class="prices"><s>89.90 €</s> 74.99 € *</div><span class="shop">ZUM SHOP</span></div>
<div class="card" style="left:395px;top:789px"><div class="photo" role="img" aria-label="Green wrap maxi dress" style="width:30px;height:132px;top:32px;background:linear-gradient(#1c8a6e,#137258)"></div><div class="badge">30%</div><div class="name">Marla Quinn</div><div class="sub">Blazer, sand</div><div class="plabel">Price</div><div class="prices"><s>89.90 €</s> 74.99 € *</div><span class="shop">ZUM SHOP</span></div>
<div class="card" style="left:577px;top:789px"><div class="photo" role="img" aria-label="Red chiffon maxi dress" style="width:36px;height:135px;top:30px;background:linear-gradient(#e83a5a,#f06a80)"></div><div class="badge">30%</div><div class="name">Marla Quinn</div><div class="sub">Blazer, sand</div><div class="plabel">Price</div><div class="prices"><s>89.90 €</s> 74.99 € *</div><span class="shop">ZUM SHOP</span></div>

<div class="more">VIEW MORE PRODUCTS <i><svg width="6" height="8" viewBox="0 0 6 8"><path d="M1 1l3 3-3 3" stroke="#fff" stroke-width="1.6" fill="none"/></svg></i></div>

<footer class="footer">
  <span class="brand-name">velunix</span>
  <span class="copy">Copyright velunix 2014.</span>
  <div class="links">Hauptmenü &nbsp;Zum Inhalt wechseln &nbsp;| &nbsp;Kontakt &nbsp;| &nbsp;AGB &nbsp;| &nbsp;Impressum &nbsp;| &nbsp;About &nbsp;| &nbsp;Services &nbsp;| &nbsp;Informieren Sie uns</div>
  <div class="note">velunix ist nicht verantwortlich für den Inhalt externer Links</div>
</footer>
</body>
</html>
```